Website Voskamp detective agency

Hi all,
After my last posted job for a logo (see attached file) I now need a website for my detective agency (Recherchebureau in Dutch)
I already have the better logo then my competitors thanks to you and your colleges working with Brandforge.
Please google the word recherchebureau to see what the competition has.
I will leave it up to you.
Bare in mind I take jobs from companies (staff steeling data or products) and private people (divorce matters etc.) so it should look very professional, trustworthy and different from the others.
My company uses creativity and new/ different ways to find the truth.
I think the logo already reflects this.
Of course I need it sliced for the website builder but if you can built it too please let me know. Then I would need a template were I can upload text and photo's etc.
Target Market(s)
Corporations
Small business
Privat people
Industry/Entity Type
Detective
Coding
Coded - Design and coding required
Number of Pages Required
5+ page
Requirements
Must have
- Responsive!
- Also this logo:
- http://www.kvbwacht.nl/wp-content/uploads/2014/05/keurmerk.png
- With the line:
- Erkend door het college van toezicht en certificering
- (This means recognized by the board of oversight)
Nice to have
- Here some extra.
- It is about website trend which I think is true.
- Please use google translate because it is in Dutch.
- http://www.lumenpost.com/archive/2014/11/17/10-webdesigntrends-voor-2015/

```html
<!DOCTYPE html>
<html lang="en">
<head>
<meta charset="utf-8">
<title>Voskamp – Recherchebureau</title>
<link href="https://fonts.googleapis.com/css2?family=Open+Sans:wght@400;600;700&family=Oswald:wght@400&display=swap" rel="stylesheet">
<style>
  :root{
    --teal:#1f9fc4;
    --teal-dark:#15809f;
    --ink:#333;
    --muted:#777;
    --dark:#232323;
    --navy:#2c3a45;
    --paper:#fff;
    --band:#f1f1f1;
    --red:#7d1418;
    --line:#dcdcdc;
  }
  *{box-sizing:border-box;margin:0;padding:0}
  html,body{width:781px;height:1200px;overflow:hidden}
  body{font-family:"Open Sans",Arial,sans-serif;color:var(--ink);background:var(--paper);position:relative;font-size:9px;line-height:1.5}
  .abs{position:absolute}
  h2{font-family:"Oswald","Arial Narrow",sans-serif;font-weight:400;font-size:17px;letter-spacing:.5px;color:#222;text-transform:uppercase}

  /* sidebar */
  .sidebar{left:0;top:0;width:205px;height:300px;padding:22px 0 0 26px}
  .brand{display:flex;align-items:center;gap:8px;margin-top:56px}
  .brand-mark{width:16px;height:16px;background:var(--navy)}
  .brand-name{font-size:21px;font-weight:700;color:var(--navy);letter-spacing:1px;text-transform:uppercase}
  .contact-line{display:flex;align-items:center;gap:7px;margin-top:8px;font-size:10px}
  .contact-line.phone{margin-top:38px;font-size:13px;font-weight:600}
  .connect{margin-top:22px;font-size:9px;color:var(--muted);text-transform:uppercase;padding-bottom:4px;border-bottom:1px solid var(--line);width:150px}
  .socials{display:flex;gap:5px;margin-top:8px}
  .socials span{width:17px;height:17px;background:var(--teal);display:block}

  /* nav */
  .nav{left:214px;top:12px;width:567px;height:28px;background:var(--dark);display:flex;align-items:stretch}
  .nav a{color:#eee;text-decoration:none;font-size:9px;text-transform:uppercase;padding:0 13px;display:flex;align-items:center}
  .nav a.active{background:var(--teal)}

  /* hero */
  .hero{left:214px;top:44px;width:567px;height:238px;background:linear-gradient(110deg,#b9c3c7 0%,#eef1f2 40%,#7d8c93 75%,#46535a 100%)}
  .dots{left:450px;top:255px;display:flex;gap:5px}
  .dots span{width:8px;height:8px;border-radius:50%;background:#fff}
  .dots span.on{background:var(--red)}

  /* welcome */
  .welcome{left:0;top:296px;width:781px;height:116px;background:var(--band);text-align:center;padding:28px 100px 0}
  .welcome p{margin-top:10px;font-size:8.5px;color:var(--muted)}

  /* services */
  .services{left:40px;top:432px;width:460px}
  .services > p{margin-top:6px;color:var(--muted);font-size:8.5px}
  .service-grid{display:flex;gap:21px;margin-top:12px}
  .service{width:219px}
  .service .photo{height:109px}
  .service h3{color:var(--teal);font-size:11px;font-weight:600;margin-top:8px}
  .service p{color:var(--muted);font-size:8.5px;margin-top:3px}
  .photo-corp{background:linear-gradient(135deg,#c7ccd0,#6d7880)}
  .photo-priv{background:linear-gradient(135deg,#d9b7a0,#8a5a4a)}

  .quick{left:513px;top:438px;width:224px;height:235px;background:var(--band);border:1px solid var(--line)}
  .quick h4{background:var(--teal);color:#fff;font-size:11px;font-weight:600;padding:6px 9px;text-transform:uppercase}
  .quick form{padding:9px}
  .field{background:#fff;border:1px solid var(--line);height:20px;margin-bottom:7px;font-size:8px;color:#999;padding:4px 6px}
  .field.msg{height:58px}
  .submit{float:right;background:var(--red);color:#fff;font-size:8px;padding:4px 10px;text-transform:uppercase}

  /* team */
  .team-bg{left:0;top:704px;width:781px;height:241px;background:linear-gradient(180deg,#4a5660,#2f3a42)}
  .team{left:0;top:720px;width:781px;text-align:center;color:#e5e5e5}
  .team h2{color:#fff}
  .team > p{font-size:8.5px;padding:6px 110px 0}
  .members{display:flex;justify-content:center;gap:28px;margin-top:22px;text-align:left}
  .member{display:flex;gap:10px;width:210px}
  .avatar{width:84px;height:84px;border-radius:50%;border:3px solid #fff;flex:none;background:linear-gradient(160deg,#c9cfd3,#6b757c)}
  .member h5{color:var(--teal);font-size:10px;font-weight:600}
  .member p{font-size:8px;color:#ddd}
  .member b{display:block;font-size:8px;color:#fff;margin-top:3px}

  /* testimonials & careers */
  .testimonials{left:40px;top:960px;width:330px}
  .quote{font-size:8.5px;color:var(--muted);margin-top:8px}
  .quote b{display:block;color:#222;margin-top:2px}
  .careers{left:396px;top:960px;width:360px}
  .careers-row{display:flex;gap:14px;margin-top:8px}
  .careers .photo{width:125px;height:102px;flex:none;background:linear-gradient(135deg,#b4c2cc,#5d6e7a)}
  .careers p{font-size:8.5px;color:var(--muted)}

  /* footer */
  .footer{left:0;top:1117px;width:781px;height:83px;background:var(--dark);text-align:center;color:#aaa;padding-top:14px}
  .footer nav{display:flex;justify-content:center;gap:16px}
  .footer nav a{color:#fff;font-size:8px;text-decoration:none;text-transform:uppercase}
  .footer p{font-size:7.5px;margin-top:10px}
</style>
</head>
<body>

<aside class="sidebar abs">
  <div class="brand"><span class="brand-mark"></span><span class="brand-name">Voskamp</span></div>
  <div class="contact-line phone">
    <svg width="12" height="12" viewBox="0 0 24 24"><path fill="#333" d="M6.6 10.8a15 15 0 0 0 6.6 6.6l2.2-2.2c.3-.3.7-.4 1-.2 1.1.4 2.3.6 3.6.6.6 0 1 .4 1 1V20c0 .6-.4 1-1 1A17 17 0 0 1 3 4c0-.6.4-1 1-1h3.5c.6 0 1 .4 1 1 0 1.3.2 2.5.6 3.6.1.3 0 .7-.2 1z"/></svg>
    123-456-7890
  </div>
  <div class="contact-line">
    <svg width="12" height="10" viewBox="0 0 24 18"><rect x="1" y="1" width="22" height="16" fill="none" stroke="#333" stroke-width="2"/><path d="M1 1l11 9 11-9" fill="none" stroke="#333" stroke-width="2"/></svg>
    info@companyname.com
  </div>
  <div class="connect">Connect us</div>
  <div class="socials"><span></span><span></span><span></span></div>
</aside>

<nav class="nav abs">
  <a class="active" href="#">Home</a>
  <a href="#">About Company</a>
  <a href="#">Our Services</a>
  <a href="#">Testimonials</a>
  <a href="#">Clients</a>
  <a href="#">Careers</a>
  <a href="#">Contact Us</a>
</nav>

<div class="hero abs" role="img" aria-label="Investigator in a suit looking at a screen of digital security icons"></div>
<div class="dots abs"><span></span><span class="on"></span><span></span><span></span></div>

<section class="welcome abs">
  <h2>Welcome to our website</h2>
  <p>We are a discreet investigation agency serving companies and private clients across the Netherlands. Our investigators combine proven methods with fresh, creative thinking to uncover facts others miss. Every case is handled with care, strict confidentiality and clear reporting, so you can make decisions based on the truth and nothing less.</p>
</section>

<section class="services abs">
  <h2>Our Services</h2>
  <p>From internal fraud and data theft to personal matters, we gather evidence that holds up. Our approach is thorough, lawful and tailored to your situation, with a fixed point of contact throughout.</p>
  <div class="service-grid">
    <article class="service">
      <div class="photo photo-corp" role="img" aria-label="Business people in a meeting"></div>
      <h3>From Companies</h3>
      <p>Staff stealing data or products? We investigate internal theft, fraud and leaks quietly, protecting your business and reputation at every step.</p>
    </article>
    <article class="service">
      <div class="photo photo-priv" role="img" aria-label="Couple talking at home"></div>
      <h3>From Private People</h3>
      <p>Divorce matters, missing persons or suspected infidelity. We listen carefully and deliver clear, reliable evidence with complete discretion and respect.</p>
    </article>
  </div>
</section>

<aside class="quick abs">
  <h4>Quick Contact</h4>
  <form>
    <div class="field">Name</div>
    <div class="field">Email Address</div>
    <div class="field">Contact No</div>
    <div class="field msg">Message</div>
    <span class="submit">Submit</span>
  </form>
</aside>

<div class="team-bg abs" role="img" aria-label="Team of professionals standing together, darkened"></div>
<section class="team abs">
  <h2>Our Team</h2>
  <p>Our investigators come from police, security and corporate backgrounds. Together they bring experience, sharp observation and new ways of looking at every case we take on.</p>
  <div class="members">
    <div class="member">
      <div class="avatar" role="img" aria-label="Portrait of team member"></div>
      <div><h5>Name Heading</h5><p>Senior investigator specialised in corporate fraud, surveillance and digital evidence, with over fifteen years in the field.</p><b>Read More</b></div>
    </div>
    <div class="member">
      <div class="avatar" role="img" aria-label="Portrait of team member"></div>
      <div><h5>Name Heading</h5><p>Expert in background checks and private cases, known for patience, precision and a calm, trustworthy approach with clients.</p><b>Read More</b></div>
    </div>
    <div class="member">
      <div class="avatar" role="img" aria-label="Portrait of team member"></div>
      <div><h5>Name Heading</h5><p>Focuses on open source research and data analysis, finding links and patterns that lead straight to the facts.</p><b>Read More</b></div>
    </div>
  </div>
</section>

<section class="testimonials abs">
  <h2>Testimonials</h2>
  <p class="quote">“ They found the source of our stock losses within weeks. Professional, discreet and always clear about progress.<b>- Name Heading</b></p>
  <p class="quote">“ I finally had the answers I needed. The team was respectful, honest and very thorough from start to finish.<b>- Name Heading</b></p>
</section>

<section class="careers abs">
  <h2>Careers with us</h2>
  <div class="careers-row">
    <div class="photo" role="img" aria-label="Team members working together at a desk"></div>
    <p>Are you curious, patient and sharp-eyed? We are always looking for investigators who think differently. Join a small team that values integrity, creativity and persistence. Send your letter and CV and tell us why you would fit in.</p>
  </div>
</section>

<footer class="footer abs">
  <nav>
    <a href="#">Home</a><a href="#">About Company</a><a href="#">Our Services</a><a href="#">Testimonials</a><a href="#">Clients</a><a href="#">Careers</a><a href="#">Contact Us</a>
  </nav>
  <p>Copyright © 2015. Company Name. All Rights Reserved.</p>
  <p style="margin-top:3px">Terms of Services | Privacy Policy</p>
</footer>

</body>
</html>
```